Building Company Business Card Design

Need a design for a business card:
It needs to have: Name, Phone, Facebook link, Website, email
i would also like a list of works we undertake:
-New Homes
-Extensions, Renovations & Bathrooms
-Decking, Carports, Sheds (Residential and Industrial)
-Carpentry
-Fences, Patios & Pergolas

Name, Phone, Facebook link, Website, email + details of services provided listed in description

```html
<!DOCTYPE html>
<html lang="en">
<head>
<meta charset="utf-8">
<title>Ridgeline Homes – Business Card</title>
<link rel="stylesheet" href="https://fonts.googleapis.com/css2?family=Montserrat:wght@500;600;700&family=Oswald:wght@400;500&display=swap">
<style>
  :root {
    --green: #35b552;
    --black: #0d0d0d;
    --charcoal: #262626;
    --white: #ffffff;
    --grey: #8a8a8a;
    --ink: #1c1c1c;
    --backdrop: #3a3a3a;
  }
  * { box-sizing: border-box; margin: 0; padding: 0; }
  html, body { width: 1200px; height: 1200px; overflow: hidden; }
  body {
    background: var(--backdrop);
    font-family: "Montserrat", Arial, sans-serif;
    position: relative;
  }
  .card {
    position: absolute;
    left: 150px;
    width: 900px;
    height: 514px;
    border-radius: 38px;
    overflow: hidden;
  }
  /* Front */
  .card-front { top: 60px; background: var(--white); }
  .person { position: absolute; left: 70px; top: 150px; }
  .person-name {
    color: var(--green);
    font-weight: 700;
    font-size: 50px;
    letter-spacing: 1px;
    line-height: 1;
  }
  .person-role {
    color: var(--ink);
    font-weight: 500;
    font-size: 26px;
    letter-spacing: 1px;
    margin-top: 6px;
  }
  .contacts { list-style: none; margin-top: 26px; }
  .contact {
    display: flex;
    align-items: center;
    gap: 16px;
    color: var(--ink);
    font-weight: 500;
    font-size: 24px;
    height: 42px;
  }
  .contact-icon { width: 28px; height: 28px; flex: none; }
  .social-dot { width: 28px; height: 28px; border-radius: 50%; background: var(--green); flex: none; }
  .brand-front {
    position: absolute;
    right: 70px;
    top: 150px;
    width: 380px;
    display: flex;
    align-items: center;
    gap: 16px;
  }
  .brand-square { width: 30px; height: 30px; background: var(--green); flex: none; }
  .brand-name {
    font-weight: 600;
    font-size: 30px;
    line-height: 1.2;
    letter-spacing: 1px;
    text-transform: uppercase;
  }
  .brand-front .brand-name { color: var(--ink); }
  .band-green {
    position: absolute; left: 0; bottom: 0;
    width: 62%; height: 34px; background: var(--green);
  }
  .band-black {
    position: absolute; right: 0; bottom: 0;
    width: 36%; height: 70px; background: var(--black);
  }
  /* Back */
  .card-back {
    top: 630px;
    background: var(--charcoal);
    border: 3px solid var(--green);
  }
  .brand-back {
    position: absolute;
    left: 0; right: 0; top: 90px;
    display: flex; justify-content: center; align-items: center; gap: 22px;
  }
  .brand-back .brand-name { color: var(--white); font-size: 46px; text-align: left; }
  .services {
    position: absolute;
    left: 60px; right: 60px; bottom: 60px;
    font-family: "Oswald", Arial Narrow, sans-serif;
    color: var(--white);
  }
  .services-title {
    color: var(--green);
    font-size: 30px;
    font-weight: 500;
    text-align: center;
    letter-spacing: 1px;
    margin-bottom: 18px;
  }
  .services-list {
    list-style: none;
    display: grid;
    grid-template-columns: 1.25fr 1fr 1fr;
    column-gap: 26px;
    row-gap: 6px;
    font-size: 19px;
    text-transform: uppercase;
    line-height: 1.3;
  }
  .service { position: relative; padding-left: 16px; }
  .service::before {
    content: ""; position: absolute; left: 0; top: 10px;
    width: 7px; height: 7px; border-radius: 50%; background: var(--green);
  }
</style>
</head>
<body>

<section class="card card-front" aria-label="Business card front">
  <div class="person">
    <h1 class="person-name">FULL NAME</h1>
    <p class="person-role">POSITION</p>
    <ul class="contacts">
      <li class="contact">
        <svg class="contact-icon" viewBox="0 0 24 24" aria-hidden="true"><path fill="#35b552" d="M6.6 10.8a15.1 15.1 0 0 0 6.6 6.6l2.2-2.2a1 1 0 0 1 1-.25 11.4 11.4 0 0 0 3.6.57 1 1 0 0 1 1 1V20a1 1 0 0 1-1 1A17 17 0 0 1 3 4a1 1 0 0 1 1-1h3.5a1 1 0 0 1 1 1c0 1.25.2 2.45.57 3.57a1 1 0 0 1-.25 1z"/></svg>
        (000) 000 0000
      </li>
      <li class="contact">
        <svg class="contact-icon" viewBox="0 0 24 24" aria-hidden="true"><rect x="2" y="5" width="20" height="14" fill="#35b552"/><path d="M2 5l10 8 10-8" fill="none" stroke="#fff" stroke-width="1.8"/></svg>
        email@company.com
      </li>
      <li class="contact">
        <svg class="contact-icon" viewBox="0 0 24 24" aria-hidden="true"><g fill="none" stroke="#35b552" stroke-width="1.8"><circle cx="12" cy="12" r="10"/><ellipse cx="12" cy="12" rx="4.5" ry="10"/><path d="M2 12h20M4 7h16M4 17h16"/></g></svg>
        www.company.com
      </li>
      <li class="contact">
        <span class="social-dot" aria-hidden="true"></span>
        @ridgelinehomes
      </li>
    </ul>
  </div>

  <div class="brand-front">
    <span class="brand-square" aria-hidden="true"></span>
    <p class="brand-name">Ridgeline Homes and Developments Pty Ltd</p>
  </div>

  <div class="band-green"></div>
  <div class="band-black"></div>
</section>

<section class="card card-back" aria-label="Business card back">
  <div class="brand-back">
    <span class="brand-square" aria-hidden="true"></span>
    <p class="brand-name">Ridgeline Homes<br>and Developments Pty Ltd</p>
  </div>

  <div class="services">
    <h2 class="services-title">SERVICES</h2>
    <ul class="services-list">
      <li class="service">New Homes</li>
      <li class="service">Decking, Carports, Sheds</li>
      <li class="service">Carpentry</li>
      <li class="service">Extensions, Renovations &amp; Bathrooms</li>
      <li class="service">(Residential and Industrial)</li>
      <li class="service">Fences, Patios &amp; Pergolas</li>
    </ul>
  </div>
</section>

</body>
</html>
```